Business Card/ Banner/ Logo/ Shirt design for (Harbour total Health Club) already have a rough idea

Hi,

I designed the business Harbour Wellbeing to create an environment where people could walk in to and feel at home, a place they could love and talk to all their friends about. I run group classes, personal training and gym activities however my interaction with clients is on a much deeper level and I help them with inspiration and life coaching improving their life with a holistic approach. I want harbour to become global and be seen as the benchmark for professionalism, yet compassion, wellness and an ora of unconditional love and care for its clients and members. I created Harbour so that people could experience life, energy and passion and begin to really love, enjoy, thrive, create and embrace their dreams and follow them.

I have made a logo that I feel best captures this mission however I used it using Microsoft word and paint so in terms of using it as a template the resolution could become distorted.

So I really reach out to the designers that want to be part of something passionate and help the harbour logo, design and vision come to physical form.

I like the logo I have created and I like purple as a feature colour, however I am open to any alterations or tweaks that your designer prowess may feel that will fit with the mission, description and vision the Harbour Wellbeing will carry of to invigorate the lives of millions.

I am also looking for a shirt design that looks professional and modern as well as fresh with life and credibility

I appreciate your time, thank you and I would love to have your inspired ideas come to life :)

Regards Tomas

If you need to contact me

Email tomasbrennick@mailvale.net
Mob 0477 213 496

Industry/Entity Type

Life Coaching

Contact Information for Business Card

Harbour Wellbeing, fitness studio and wellness centre

Logo styles of interest
Emblem Logo
Pictorial/Combination Logo
Abstract Logo
Character Logo
Wordmark Logo
Lettermark Logo
Requirements
Nice to have
• Purple, original "H" logo
Tag line "The Pulse of Vitality"

```html
<!DOCTYPE html>
<html lang="en">
<head>
<meta charset="utf-8">
<title>Harbour Wellbeing – Business Card</title>
<link rel="stylesheet" href="https://fonts.googleapis.com/css2?family=Open+Sans:wght@400;600&display=swap">
<style>
  :root {
    --page: #2b2b2d;
    --purple-deep: #2f1452;
    --purple: #3d1c66;
    --lavender: #7d58b0;
    --lavender-soft: #a58ad0;
    --ink: #3a1d5e;
    --card-white: #ffffff;
    --card-grey: #e9e9ec;
    --band-text: #d8d2e2;
  }
  * { margin: 0; padding: 0; box-sizing: border-box; }
  html, body {
    width: 1200px; height: 900px; overflow: hidden;
    background: var(--page);
    font-family: "Open Sans", Arial, sans-serif;
  }
  .canvas {
    width: 1200px; height: 900px;
    display: flex; flex-direction: column;
    align-items: center; justify-content: center; gap: 40px;
  }
  .card {
    position: relative;
    width: 660px; height: 377px;
    border-radius: 30px;
    overflow: hidden;
  }
  /* Back side */
  .card-back {
    background: linear-gradient(135deg, var(--purple) 0%, var(--purple-deep) 100%);
    display: flex; align-items: center; justify-content: center;
  }
  .brand { display: flex; flex-direction: column; align-items: flex-start; }
  .brand-row { display: flex; align-items: center; gap: 14px; }
  .brand-mark { width: 34px; height: 34px; }
  .brand-name { font-weight: 600; font-size: 34px; letter-spacing: 0.2px; }
  .tagline {
    margin-top: 6px; margin-left: 48px;
    font-size: 13px; font-weight: 600; letter-spacing: 3.2px; text-transform: uppercase;
  }
  .card-back .brand-mark { background: var(--lavender-soft); }
  .card-back .brand-name { color: var(--card-white); }
  .card-back .tagline { color: var(--lavender-soft); }

  /* Front side */
  .card-front {
    background: linear-gradient(160deg, var(--card-white) 40%, var(--card-grey) 100%);
  }
  .front-wave { position: absolute; inset: 0; width: 100%; height: 100%; }
  .card-front .brand { position: absolute; left: 44px; top: 140px; }
  .card-front .brand-mark { background: var(--ink); }
  .card-front .brand-name { color: var(--ink); font-size: 30px; }
  .card-front .tagline { color: var(--lavender); font-size: 11px; letter-spacing: 2.6px; }

  .contact { position: absolute; left: 410px; top: 28px; color: var(--ink); }
  .contact-name { font-size: 21px; font-weight: 600; }
  .contact-role { font-size: 14px; margin-bottom: 12px; }
  .contact-list { list-style: none; font-size: 13px; line-height: 17px; }
  .contact-list li { display: flex; align-items: flex-start; gap: 9px; margin-bottom: 2px; }
  .contact-list li.gap { margin-top: 8px; }
  .icon { width: 13px; height: 14px; flex: none; margin-top: 2px; fill: var(--ink); }
  .band-text {
    position: absolute; left: 0; right: 0; bottom: 22px;
    text-align: center; color: var(--band-text);
    font-size: 16px; letter-spacing: 0.8px; text-transform: uppercase;
  }
</style>
</head>
<body>
<main class="canvas">

  <section class="card card-back" aria-label="Card back">
    <div class="brand">
      <div class="brand-row">
        <span class="brand-mark"></span>
        <span class="brand-name">Harbour Wellbeing</span>
      </div>
      <span class="tagline">The pulse of vitality</span>
    </div>
  </section>

  <section class="card card-front" aria-label="Card front">
    <svg class="front-wave" viewBox="0 0 660 377" preserveAspectRatio="none" aria-hidden="true">
      <path d="M0,305 C220,292 460,262 660,215 L660,377 L0,377 Z" fill="var(--purple)"/>
      <path d="M0,282 C180,274 360,256 470,232 C370,262 190,288 0,297 Z" fill="var(--lavender)"/>
    </svg>

    <div class="brand">
      <div class="brand-row">
        <span class="brand-mark"></span>
        <span class="brand-name">Harbour Wellbeing</span>
      </div>
      <span class="tagline">The pulse of vitality</span>
    </div>

    <div class="contact">
      <p class="contact-name">Martin Kessley</p>
      <p class="contact-role">managing director</p>
      <ul class="contact-list">
        <li>
          <svg class="icon" viewBox="0 0 12 14"><path d="M6 0a5 5 0 0 0-5 5c0 3.5 5 9 5 9s5-5.5 5-9a5 5 0 0 0-5-5zm0 7a2 2 0 1 1 0-4 2 2 0 0 1 0 4z"/></svg>
          <span>48 Quayline Road<br>Marrowby, Ohio 44021</span>
        </li>
        <li>
          <svg class="icon" viewBox="0 0 12 14"><path d="M3 0h6a1 1 0 0 1 1 1v12a1 1 0 0 1-1 1H3a1 1 0 0 1-1-1V1a1 1 0 0 1 1-1zm0 2v9h6V2z"/></svg>
          <span>0477 213 496</span>
        </li>
        <li>
          <svg class="icon" viewBox="0 0 12 14"><path d="M3 1h6v3H3zM1 5h10v6H9v2H3v-2H1zm3 4v3h4V9z"/></svg>
          <span>0477 213 497</span>
        </li>
        <li class="gap">
          <svg class="icon" viewBox="0 0 12 14"><path d="M0 3h12v8H0zm1 1v.4L6 8l5-3.6V4z"/></svg>
          <span>info@harbourwellbeing.net</span>
        </li>
        <li>
          <svg class="icon" viewBox="0 0 12 14"><circle cx="6" cy="7" r="5.5"/><path d="M0.5 7h11M6 1.5c-2.5 3-2.5 8 0 11M6 1.5c2.5 3 2.5 8 0 11" stroke="#fff" stroke-width="0.8" fill="none"/></svg>
          <span>www.harbourwellbeing.net</span>
        </li>
      </ul>
    </div>

    <p class="band-text">Fitness studio and wellness centre</p>
  </section>

</main>
</body>
</html>
```